Broschüre für Trainer für Resilienz
Zielgruppe
Wir sind ein Zusammenschluss von zwei selbstständigen Trainern, welche sich spezialisiert haben auf den Bereich Resilienz in Unternehmen.
Insgesamt haben wir hierfür 4 Säulen erarbeitet:
1. Resilienz - Training
2. Psychologische Beratung
3. Burnout - Prophylaxe
4. Weiterbildungen
Weitere Informationen finden Sie in der angehängten Datei mit dem Titel 'flyer_Inhalt'.
Als Zielgruppe haben wir mittelständische und große Unternehmen im Blick, hierbei jeweils die Mitarbeiter und Führungskräfte
Aufgabenstellung
Wir stellen uns eine Broschüre im DIN-A4 - Format vor, 6 Seiten mit Wickelfalz.
Eine Broschüre, welche bei Kunden großen Anklang gefunden hat, war meine Dozent4.1 - Broschüre, welche ich als Beispiel ebenfalls hochgeladen habe.
Nach ein paar Missverständnissen möchte ich das Format an dieser Stelle genauer beschreiben:
Es geht um einen Flyer/ eine Broschüre, welche im DIN-A4-Format gestaltet wird. Hierbei nicht ein DIN-A4-Format im Querformat, sondern DREI DIN-A4-Seiten, welche mit einer Wickelfalz verbunden sind und somit 6 DIN-A4-Flächen zum Bedrucken bilden.

```html
<!DOCTYPE html>
<html lang="de">
<head>
<meta charset="utf-8">
<title>Innenstark4Teams – Broschüre Innenseite</title>
<link rel="stylesheet" href="https://fonts.googleapis.com/css2?family=Open+Sans:wght@300;400;600;700&display=swap">
<style>
  :root {
    --brand-blue: #1b4f93;
    --shield: #7d93b8;
    --ink: #1e1e1e;
    --muted: #6a6a6a;
    --dark-panel: #3a3a3c;
    --white: #ffffff;
  }
  * { margin: 0; padding: 0; box-sizing: border-box; }
  html, body { width: 1200px; height: 566px; overflow: hidden; background: var(--white); }
  body { font-family: "Open Sans", sans-serif; color: var(--ink); }
  .spread { position: relative; width: 1200px; height: 566px; overflow: hidden; }
  .panel { position: absolute; top: 0; height: 566px; width: 400px; }
  .panel--pillars { left: 0; background: var(--white); }
  .panel--trainers { left: 400px; background: var(--white); }
  .panel--cover { left: 800px; background: var(--dark-panel); }

  .photo { position: absolute; }
  .photo--team { left: 0; top: 0; width: 400px; height: 243px;
    background: linear-gradient(135deg, #dfe6ee 0%, #c9b8a8 45%, #e8eef4 100%); }
  .photo--trainer-a { left: 0; top: 0; width: 400px; height: 243px;
    background: radial-gradient(ellipse at 70% 60%, #3b2a28 0%, #6a4f3a 35%, #b8946b 75%, #c8a57e 100%); }
  .photo--trainer-b { left: 0; top: 243px; width: 400px; height: 234px;
    background: radial-gradient(ellipse at 70% 55%, #2a2228 0%, #4a3f4a 40%, #5f5560 100%); }
  .photo--leader { left: 0; top: 0; width: 400px; height: 404px;
    background: radial-gradient(ellipse at 65% 40%, #6a6a6c 0%, #4a4a4c 50%, #333335 100%); }

  .pillars-title { position: absolute; left: 54px; top: 258px; font-size: 22.5px; font-weight: 300;
    line-height: 26px; color: var(--brand-blue); }
  .pillars-title strong { font-weight: 700; }
  .pillar-grid { position: absolute; left: 54px; top: 327px; width: 275px; height: 198px; }
  .pillar { position: absolute; width: 134px; height: 95px; background: var(--brand-blue);
    color: var(--white); font-size: 12px; font-weight: 300; text-align: center; line-height: 15px;
    display: flex; flex-direction: column; align-items: center; justify-content: center; padding-top: 14px; }
  .pillar svg { position: absolute; top: 22px; left: 50%; margin-left: -6px; }
  .pillar--1 { left: 0; top: 0; }
  .pillar--2 { left: 141px; top: 0; }
  .pillar--3 { left: 0; top: 103px; }
  .pillar--4 { left: 141px; top: 103px; }
  .pillar--3, .pillar--4 { padding-top: 20px; }
  .pillar-joins { position: absolute; left: 0; top: 0; }

  .section-title { position: absolute; left: 27px; top: 22px; color: var(--white);
    font-size: 22px; font-weight: 400; letter-spacing: 0.3px; }
  .bio { position: absolute; left: 0; width: 232px; background: rgba(205,200,215,0.55);
    padding: 16px 10px 0 27px; color: #1a1a1a; }
  .bio--a { top: 160px; height: 83px; }
  .bio--b { top: 394px; height: 83px; padding-left: 30px; }
  .bio h3 { font-size: 9.5px; font-weight: 400; margin-bottom: 8px; }
  .bio p { font-size: 5.6px; line-height: 9.4px; }

  .contact { position: absolute; top: 489px; font-size: 9.5px; line-height: 12.8px; }
  .contact--labels { left: 27px; color: var(--muted); }
  .contact--values { left: 76px; }
  .contact--post { left: 221px; }
  .contact--post .label { color: var(--muted); }

  .brand-box { position: absolute; left: 1px; top: 337px; width: 337px; height: 68px;
    background: var(--brand-blue); color: var(--white); font-size: 30px; font-weight: 600;
    padding: 16px 0 0 28px; letter-spacing: 0.2px; }
  .benefits { position: absolute; left: 93px; top: 432px; list-style: none; color: var(--white); }
  .benefits li { position: relative; font-size: 10.6px; line-height: 16px; margin-bottom: 10px; }
  .benefits li svg { position: absolute; left: -29px; top: 2px; }
  .benefits li:first-child { font-weight: 300; padding-left: 2px; }
  .benefits li:last-child { font-weight: 600; }
</style>
</head>
<body>
<main class="spread">

  <section class="panel panel--pillars">
    <div class="photo photo--team" role="img" aria-label="Foto: Teammitglieder legen ihre Hände übereinander"></div>
    <h2 class="pillars-title">Die vier Säulen für Ihr<br><strong>resilientes</strong> Unternehmen</h2>
    <div class="pillar-grid">
      <div class="pillar pillar--1">
        <svg width="12" height="14" viewBox="0 0 12 14"><path d="M6 0 L12 2 V7 C12 10 9 12.5 6 14 C3 12.5 0 10 0 7 V2 Z" fill="var(--shield)"/></svg>
        Resilienz-Training
      </div>
      <div class="pillar pillar--2">
        <svg width="12" height="14" viewBox="0 0 12 14"><path d="M6 0 L12 2 V7 C12 10 9 12.5 6 14 C3 12.5 0 10 0 7 V2 Z" fill="var(--shield)"/></svg>
        Burnout-<br>Prophylaxe
      </div>
      <div class="pillar pillar--3">
        <svg width="12" height="14" viewBox="0 0 12 14"><path d="M6 0 L12 2 V7 C12 10 9 12.5 6 14 C3 12.5 0 10 0 7 V2 Z" fill="var(--shield)"/></svg>
        Psychologische<br>Beratung
      </div>
      <div class="pillar pillar--4">
        <svg width="12" height="14" viewBox="0 0 12 14"><path d="M6 0 L12 2 V7 C12 10 9 12.5 6 14 C3 12.5 0 10 0 7 V2 Z" fill="var(--shield)"/></svg>
        Weiterbildungen
      </div>
      <svg class="pillar-joins" width="275" height="198" viewBox="0 0 275 198">
        <path d="M134 23 L141 30 L134 37 Z" fill="var(--brand-blue)"/>
        <path d="M141 23 L148 30 L141 37 Z" fill="var(--white)"/>
        <path d="M102 95 L109 88 L116 95 Z" fill="var(--white)"/>
        <path d="M102 103 L109 96 L116 103 Z" fill="var(--brand-blue)"/>
        <path d="M238 95 L245 102 L252 95 Z" fill="var(--brand-blue)"/>
        <path d="M238 103 L245 110 L252 103 Z" fill="var(--white)"/>
        <path d="M134 148 L127 155 L134 162 Z" fill="var(--white)"/>
        <path d="M141 148 L134 155 L141 162 Z" fill="var(--brand-blue)"/>
      </svg>
    </div>
  </section>

  <section class="panel panel--trainers">
    <div class="photo photo--trainer-a" role="img" aria-label="Porträtfoto der Trainerin vor goldbraunem Hintergrund"></div>
    <div class="photo photo--trainer-b" role="img" aria-label="Porträtfoto des Trainers vor dunklem Hintergrund"></div>
    <h2 class="section-title">Ihre Trainer</h2>
    <article class="bio bio--a">
      <h3>Dipl. Psych. Marlene Hofstetter</h3>
      <p>Inhaberin und Leiterin der Praxisgemeinschaft am Lindenhof,<br>Psychologische Psychotherapeutin, Kinder- und Jugendlichen-<br>Psychotherapie, Zertifizierte Trainerin für Autogenes Training,<br>Mehrjährige Erfahrung als Trainerin</p>
    </article>
    <article class="bio bio--b">
      <h3>Jonas Michael Brenner, M.A.</h3>
      <p>Mehrjährige Erfahrung als Trainer, Zertifizierter Mediator mit<br>mehrjähriger Berufserfahrung, Psychotherapeut in der<br>Ausbildung zum Kinder- und Jugendlichenpsychotherapeuten,<br>Internationale Berufs- und Studienerfahrung</p>
    </article>
    <div class="contact contact--labels">Telefon<br>Fax<br>E-Mail</div>
    <div class="contact contact--values">04521 18 40 273<br>04521 37 60 519<br>info@innenstark4teams.de</div>
    <div class="contact contact--post"><span class="label">Post</span><br>innenstark4teams<br>Lindenweg 12</div>
  </section>

  <section class="panel panel--cover">
    <div class="photo photo--leader" role="img" aria-label="Foto: Geschäftsmann im Anzug vor grauer Wand, zeigt Stärke"></div>
    <h1 class="brand-box">Innenstark4Teams</h1>
    <ul class="benefits">
      <li>
        <svg width="12" height="14" viewBox="0 0 12 14"><path d="M6 0 L12 2 V7 C12 10 9 12.5 6 14 C3 12.5 0 10 0 7 V2 Z" fill="#8a8a8c"/></svg>
        Leistungsfähige Mitarbeiter sichern<br>den Erfolg Ihres Unternehmens.
      </li>
      <li>
        <svg width="12" height="14" viewBox="0 0 12 14"><path d="M6 0 L12 2 V7 C12 10 9 12.5 6 14 C3 12.5 0 10 0 7 V2 Z" fill="#8a8a8c"/></svg>
        Nutzen Sie die Vorteile der gesetzlich<br>geförderten Gesundheitsvorsorge für<br>Ihr Team.
      </li>
    </ul>
  </section>

</main>
</body>
</html>
```